Hollow Breeze - New Product needs a Label

We need a package label for a new project that will come to market soon. The company is based in Canada and will need to show 'Made in Canada' with a Canadian flag.

The product is called Hollow Breeze. It is an odour eliminator. It will be in a dark brown plastic container that can be opened and left open in a room.

It can be used to help eliminate a number of different types of smoke; cigarette, pot or even fireplace smoke. We believe that 'no one should know what you smoke'.

We would like to see designs that reflect the intent of the product - to cover smoke. So far we've only thought that smokey colours like smokey green, smokey lavender and smokey grey or other grey tone colours would make sense. Update: I have removed the image that I 'doodled' on my own because I think it's been taken too literally. Please give me a fresh look at what an odor eliminator image could be.

Label dimensions are 11.25"x2.25"
Key wording:

Product Name: Hollow Breeze
Tag line: No one needs to know what you smoke
Also needs to include:
Directions
Remove the lid and place the container in any room where smoke is present. The contents will evaporate, neutralizing odours.

Net Wt. 14 0z. - 400 G
A spot for adding a bar code for scanners

Target Market(s)

Cigarette smokers / pot smokers / people with fire places or people who share a home with any of those categories

Requirements
Must have
• a label that fits the dimensions 11.25"x2.25" and the text / components outlined in the description
Nice to have
• A bit of humour, a sense of natural products

```html
<!DOCTYPE html>
<html lang="en">
<head>
<meta charset="utf-8">
<title>Hollow Breeze – Label</title>
<link rel="stylesheet" href="https://fonts.googleapis.com/css2?family=Open+Sans:wght@400;600;700&display=swap">
<style>
  :root {
    --stage: #1b1b1c;
    --label-black: #050506;
    --ink: #f2f2f2;
    --ink-soft: #d9d9d9;
    --flag-red: #d52b1e;
    --flag-white: #ffffff;
    --code-spot: #ffffff;
  }
  * { margin: 0; padding: 0; box-sizing: border-box; }
  html, body {
    width: 1200px;
    height: 2179px;
    overflow: hidden;
    background: var(--stage);
    font-family: "Open Sans", Arial, sans-serif;
  }
  .label {
    position: absolute;
    left: 85px;
    top: 828px;
    width: 1032px;
    height: 222px;
    background: var(--label-black);
    overflow: hidden;
  }
  .smoke {
    position: absolute;
    top: 0;
    height: 222px;
  }
  .smoke--left {
    left: 0;
    width: 470px;
    background:
      radial-gradient(ellipse 50% 60% at 22% 55%, rgba(31,163,122,0.32), transparent 70%),
      radial-gradient(ellipse 45% 55% at 58% 38%, rgba(46,79,192,0.30), transparent 70%),
      radial-gradient(ellipse 40% 45% at 85% 72%, rgba(90,63,176,0.28), transparent 70%);
  }
  .smoke--right {
    left: 490px;
    width: 460px;
    background:
      radial-gradient(ellipse 40% 45% at 15% 72%, rgba(90,63,176,0.28), transparent 70%),
      radial-gradient(ellipse 45% 55% at 42% 38%, rgba(46,79,192,0.30), transparent 70%),
      radial-gradient(ellipse 50% 60% at 78% 55%, rgba(31,163,122,0.32), transparent 70%);
  }
  .brand {
    position: absolute;
    left: 369px;
    top: 0;
    width: 220px;
    height: 222px;
    text-align: center;
    color: var(--ink);
  }
  .brand__name {
    margin-top: 34px;
    font-size: 26px;
    font-weight: 600;
    letter-spacing: 1px;
    line-height: 1.1;
    text-transform: uppercase;
    white-space: nowrap;
  }
  .brand__mark {
    display: block;
    margin: 22px auto 26px;
    width: 26px;
    height: 26px;
    border-radius: 50%;
    background: var(--ink);
  }
  .brand__tagline {
    font-size: 10px;
    font-weight: 700;
    line-height: 1.4;
    letter-spacing: 0.4px;
    text-transform: uppercase;
  }
  .brand__weight {
    margin-top: 16px;
    font-size: 8px;
    font-weight: 600;
    color: var(--ink-soft);
  }
  .info-panel {
    position: absolute;
    left: 885px;
    top: 81px;
    width: 200px;
    height: 60px;
    transform: rotate(-90deg);
    color: var(--ink);
    display: flex;
    gap: 6px;
  }
  .info-panel__code {
    flex: 0 0 64px;
    display: flex;
    flex-direction: column;
    justify-content: space-between;
  }
  .code-spot {
    width: 52px;
    height: 40px;
    background: var(--code-spot);
  }
  .origin {
    display: flex;
    align-items: center;
    gap: 3px;
    font-size: 6px;
    line-height: 1;
    white-space: nowrap;
  }
  .origin strong { font-weight: 700; }
  .flag {
    display: flex;
    width: 14px;
    height: 7px;
    flex: 0 0 14px;
  }
  .flag__band { background: var(--flag-red); flex: 1; }
  .flag__field { background: var(--flag-white); flex: 2; }
  .directions {
    flex: 1;
    font-size: 6.5px;
    line-height: 1.35;
  }
  .directions__heading { font-weight: 700; }
</style>
</head>
<body>
  <section class="label">
    <div class="smoke smoke--left" role="img" aria-label="Line-drawn swirling cloud ornament fading from smoky green to blue and lavender"></div>
    <div class="smoke smoke--right" role="img" aria-label="Line-drawn swirling cloud ornament fading from lavender to blue and smoky green"></div>

    <div class="brand">
      <h1 class="brand__name">Hollow Breeze</h1>
      <span class="brand__mark"></span>
      <p class="brand__tagline">No one needs to know<br>what you smoke</p>
      <p class="brand__weight">Net Wt. 14 Oz. - 400 G</p>
    </div>

    <aside class="info-panel">
      <div class="info-panel__code">
        <div class="code-spot"></div>
        <p class="origin">
          <span>MADE IN <strong>CANADA</strong></span>
          <span class="flag" role="img" aria-label="Canadian flag"><span class="flag__band"></span><span class="flag__field"></span><span class="flag__band"></span></span>
        </p>
      </div>
      <div class="directions">
        <p class="directions__heading">Directions</p>
        <p>Remove the lid and place the container in any room where smoke is present. The contents will evaporate, neutralizing odours.</p>
      </div>
    </aside>
  </section>
</body>
</html>
```